Corvid Lens Studio Business Card Design

I need a business card designed for a photography business based in Perth, Western Australia called Corvid Lens Studio.

We specialise in wedding, event photography and portrait photography.

The business card must borrow the style of the attached logo.

The hex codes for the colours in the logo are:
#ED1D85 - Pink
#89C23E - Green
#37282F - Black

The name on the card will be:
Name: Tobiah
Phone: 0417395268
Website: www.corvidlensstudio.com.au
Facebook: corvidlensstudio

I am open and happy to accept creative concepts.

Industry/Entity Type

Business

```html
<!DOCTYPE html>
<html lang="en">
<head>
<meta charset="utf-8">
<title>Corvid Lens Studio – Business Card</title>
<link href="https://fonts.googleapis.com/css2?family=Raleway:wght@400&family=Tinos:wght@400;700&display=swap" rel="stylesheet">
<style>
  :root {
    --brand-pink: #ED1D85;
    --brand-green: #89C23E;
    --brand-black: #37282F;
    --paper: #ffffff;
    --backdrop: #d9d9d9;
    --band: rgba(255, 255, 255, 0.7);
    --muted: #5a5557;
  }
  * { box-sizing: border-box; margin: 0; padding: 0; }
  html, body { width: 992px; height: 1200px; overflow: hidden; }
  body { background: var(--backdrop); position: relative; font-family: "Raleway", sans-serif; }

  .card { position: absolute; overflow: hidden; }

  /* Front */
  .card-front {
    left: 75px; top: 66px; width: 870px; height: 496px;
    background: var(--paper);
    border-style: solid; border-color: var(--brand-green);
    border-width: 24px 28px 24px 28px;
  }
  .front-mark {
    position: absolute; left: 50%; top: 132px; width: 124px; height: 124px;
    margin-left: -62px;
  }
  .front-wordmark {
    position: absolute; left: 0; right: 0; top: 294px;
    text-align: center; font-size: 19px; letter-spacing: 16px;
    color: var(--brand-black); text-transform: uppercase;
    padding-left: 16px;
  }

  /* Back */
  .card-back { left: 72px; top: 645px; width: 873px; height: 502px; }
  .back-photo {
    position: absolute; inset: 0;
    background:
      radial-gradient(ellipse 190px 200px at 27% 78%, rgba(255,255,255,0.95), rgba(255,255,255,0) 100%),
      radial-gradient(ellipse 150px 130px at 30% 30%, rgba(222,196,150,0.55), rgba(222,196,150,0) 100%),
      linear-gradient(180deg, rgba(255,255,255,0.25) 0%, rgba(255,255,255,0) 12%),
      linear-gradient(100deg, #e2dfbe 0%, #e6e3c6 18%, #c6d59a 40%, #7db33e 54%, #4f9a1e 68%, #5aa62a 84%, #8cc55a 100%);
  }
  .holder-name {
    position: absolute; right: 42px; top: 30px;
    font-family: "Tinos", serif; font-weight: 400; font-size: 80px; line-height: 1;
    color: var(--paper); text-shadow: 2px 3px 4px rgba(0,0,0,0.45);
  }
  .holder-phone {
    position: absolute; right: 42px; top: 106px;
    font-family: "Tinos", serif; font-weight: 400; font-size: 30px; line-height: 1;
    color: var(--paper); text-shadow: 1px 2px 3px rgba(0,0,0,0.45);
  }
  .contact-band {
    position: absolute; left: 0; right: 0; top: 308px; bottom: 14px;
    background: var(--band);
  }
  .back-mark { position: absolute; left: 138px; top: 335px; width: 80px; height: 80px; }
  .back-wordmark {
    position: absolute; left: 15px; top: 432px;
    font-size: 12px; letter-spacing: 9px; color: var(--muted);
    text-transform: uppercase;
  }
  .contact-list { position: absolute; right: 44px; top: 322px; list-style: none; }
  .contact-item {
    display: flex; align-items: center; justify-content: flex-end;
    height: 52px;
    font-family: "Tinos", serif; font-weight: 700; font-size: 28px; letter-spacing: 1.2px;
    color: var(--brand-black);
  }
  .contact-item.phone { font-size: 29px; letter-spacing: 1.5px; }
  .contact-icon { width: 32px; height: 32px; margin-left: 24px; flex: none; }
</style>
</head>
<body>

<section class="card card-front" aria-label="Card front">
  <svg class="front-mark" viewBox="0 0 124 124" aria-hidden="true">
    <circle cx="62" cy="62" r="58" fill="none" stroke="var(--brand-pink)" stroke-width="4"/>
  </svg>
  <p class="front-wordmark">Corvid Lens Studio</p>
</section>

<section class="card card-back" aria-label="Card back">
  <div class="back-photo" role="img" aria-label="Wedding portrait photograph of a couple seated by a lake among tall green reeds"></div>
  <h1 class="holder-name">Tobiah</h1>
  <p class="holder-phone">0417395268</p>

  <div class="contact-band"></div>
  <svg class="back-mark" viewBox="0 0 80 80" aria-hidden="true">
    <circle cx="40" cy="40" r="36" fill="none" stroke="var(--brand-pink)" stroke-width="3"/>
  </svg>
  <p class="back-wordmark">Corvid Lens Studio</p>

  <ul class="contact-list">
    <li class="contact-item social">corvidlensstudio
      <svg class="contact-icon" viewBox="0 0 32 32" aria-hidden="true"><circle cx="16" cy="16" r="15" fill="var(--brand-black)"/></svg>
    </li>
    <li class="contact-item website">www.corvidlensstudio.com.au
      <svg class="contact-icon" viewBox="0 0 32 32" aria-hidden="true">
        <rect x="2" y="4" width="28" height="19" fill="none" stroke="var(--brand-black)" stroke-width="3"/>
        <rect x="13" y="23" width="6" height="4" fill="var(--brand-black)"/>
        <rect x="8" y="27" width="16" height="3" fill="var(--brand-black)"/>
      </svg>
    </li>
    <li class="contact-item phone">0417395268
      <svg class="contact-icon" viewBox="0 0 32 32" aria-hidden="true">
        <path d="M2 10 Q16 1 30 10 L27 14 L22 12 L21 9 Q16 7 11 9 L10 12 L5 14 Z" fill="var(--brand-black)"/>
        <path d="M9 14 L23 14 L29 28 L3 28 Z" fill="var(--brand-black)"/>
        <circle cx="16" cy="21" r="3.5" fill="var(--paper)"/>
      </svg>
    </li>
  </ul>
</section>

</body>
</html>
```